Vostran, Pemmel & Co.
Project: Brochure
Brochure
Individuals, Corporations, Non - Profit organizations & small business and Ledgerfox users.
New Logo Attached Word File I would like either a tri fold brochure but leaning twards a brochure that is 11 inch height by 5 inch wide which would have 4 pages - Cover, 2 inside pages & back cover. Probably a better fit since I do not have a lot of content. Maybe a picture that would be appropriate also.

```html
<!DOCTYPE html>
<html lang="en">
<head>
<meta charset="utf-8">
<title>Vostran, Pemmel &amp; Co. — Brochure</title>
<link rel="stylesheet" href="https://fonts.googleapis.com/css2?family=Libre+Baskerville:wght@400;700&family=Source+Sans+3:wght@300;400;600&display=swap">
<style>
:root{
  --bg:#ece7e1;
  --brown:#3f2415;
  --brown-mid:#5e3620;
  --orange:#d9772b;
  --orange-soft:#e9a268;
  --peach:#f5dcc4;
  --cream:#fbf4ec;
  --ink:#3b302a;
  --muted:#7d6e63;
  --line:#e2cdb8;
}
*{box-sizing:border-box;margin:0;padding:0}
html,body{width:1200px;height:1037px;overflow:hidden;background:var(--bg)}
body{font-family:"Source Sans 3",Arial,sans-serif;color:var(--ink);position:relative}
.spread{position:absolute;left:30px;width:1140px;height:470px;display:flex;box-shadow:0 4px 14px rgba(0,0,0,.18);background:#fff}
.spread.outer{top:30px}
.spread.inner{top:537px}
.panel{position:relative;width:285px;height:470px;overflow:hidden;border-right:1px solid #eee}
.panel:last-child{border-right:none}
.serif{font-family:"Libre Baskerville",Georgia,serif}
.photo{position:absolute}
.copy{font-size:7px;line-height:1.45;color:var(--ink)}
.copy p{margin-bottom:6px}
.brand{display:flex;align-items:center;gap:8px}
.brand-mark{width:26px;height:26px;background:var(--orange);flex:none}
.brand-name{font-family:"Libre Baskerville",Georgia,serif;font-size:12px;color:var(--brown)}
.title{font-family:"Source Sans 3",Arial,sans-serif;font-weight:300;color:var(--orange);line-height:1}
.subtitle{font-size:8px;letter-spacing:4px;text-transform:uppercase;color:var(--brown);margin-top:3px}
.bullets{list-style:none}
.bullets li{font-size:8.5px;padding:4px 0 4px 14px;position:relative;color:var(--ink)}
.bullets li::before{content:"";position:absolute;left:0;top:7px;width:7px;height:7px;background:var(--brown)}
.checks{list-style:none}
.checks li{font-size:9px;padding:6px 0 6px 20px;position:relative;color:var(--brown);border-bottom:1px solid var(--line)}
.checks svg{position:absolute;left:0;top:6px}

/* Page 1 */
.p1 .head{padding:18px 16px 10px}
.p1 .tag{font-size:7px;color:var(--muted);margin-top:6px;letter-spacing:.5px}
.p1 .copy{padding:4px 16px}
.p1 .bullets{padding:0 16px}
.p1 .bullets li{font-size:7.5px;padding:2px 0 2px 12px}
.p1 .bullets li::before{top:5px;width:5px;height:5px;background:var(--orange)}
.p1 .photo{left:0;bottom:0;width:285px;height:130px;background:linear-gradient(135deg,#b67a3a,#e7b86d 55,#8a5325)}

/* Page 2 */
.p2{background:linear-gradient(180deg,var(--cream),var(--peach))}
.p2 .photo{left:0;top:0;width:90px;height:470px;background:linear-gradient(180deg,#c9a78a,#8c6a52)}
.p2 .body{position:absolute;left:104px;top:24px;right:16px}
.p2 .title{font-size:34px}
.p2 .checks{margin-top:18px}

/* Back */
.back .band{background:linear-gradient(180deg,var(--brown-mid),var(--brown));color:var(--cream);padding:22px 18px 18px}
.back .band p{font-family:"Libre Baskerville",Georgia,serif;font-size:12px;line-height:1.45}
.back .band p span{color:var(--orange-soft)}
.back .addr{padding:14px 18px;font-size:8px;line-height:1.6;color:var(--ink)}
.back .map{left:18px;top:210px;width:200px;height:140px;background:linear-gradient(135deg,#e8e3da,#cfc6b8)}
.back .badge{position:absolute;left:228px;top:210px;width:40px;height:60px;background:var(--brown-mid)}
.back .web{position:absolute;left:18px;bottom:22px;font-size:9px;color:var(--brown)}

/* Front cover */
.front{background:linear-gradient(180deg,var(--brown-mid),var(--brown) 60%)}
.front .brand{padding:22px 18px 0}
.front .brand-name{color:var(--cream);font-size:13px}
.front .claim{font-family:"Libre Baskerville",Georgia,serif;color:var(--orange-soft);font-size:17px;line-height:1.3;padding:22px 18px 16px}
.front .photo{left:0;top:160px;width:285px;height:170px;background:linear-gradient(135deg,#f1e6d6,#c79a6a)}
.front .names{position:absolute;left:18px;top:348px;font-family:"Libre Baskerville",Georgia,serif;font-size:8.5px;color:var(--cream);line-height:2;letter-spacing:.5px}
.front .web{position:absolute;left:18px;bottom:20px;font-size:9px;color:var(--orange-soft)}

/* Page 3 */
.p3 .head{padding:22px 18px 0}
.p3 .title{font-size:40px}
.p3 .photo{left:18px;top:90px;width:249px;height:110px;background:linear-gradient(135deg,#f2f0ec,#b8b3ab)}
.p3 .bullets{position:absolute;left:18px;top:212px;right:18px}
.p3 .client{position:absolute;left:18px;top:362px;right:18px}
.p3 .client h3{font-family:"Libre Baskerville",Georgia,serif;font-weight:400;color:var(--orange);font-size:13px;margin-bottom:5px}

/* Page 4 */
.p4 .photo{inset:0;background:linear-gradient(160deg,#e6dfd6,#9d8a78 60%,#5d4a3c)}
.p4 .strip{position:absolute;left:0;right:0;bottom:0;height:14px;background:var(--orange)}

/* Page 5 */
.p5 .head{padding:24px 18px 0}
.p5 .title{font-size:28px}
.p5 .copy{padding:18px 18px 0;font-size:7.5px}
.p5 .rule{height:3px;background:var(--orange);margin:6px 18px 0;width:40px}

/* Page 6 */
.p6 .vertical{position:absolute;left:-118px;top:230px;transform:rotate(-90deg);width:280px;text-align:center;font-size:32px;font-weight:300;color:var(--orange)}
.p6 .title{position:absolute;left:58px;top:20px;font-size:30px;color:var(--brown)}
.p6 .staff{position:absolute;left:58px;right:14px;top:64px}
.member{display:flex;gap:8px;margin-bottom:14px}
.member .portrait{width:44px;height:56px;flex:none;background:linear-gradient(180deg,#cfc2b4,#8f7b69)}
.member h4{font-family:"Libre Baskerville",Georgia,serif;font-weight:400;font-size:8px;color:var(--brown);margin-bottom:3px}
.member p{font-size:6.5px;line-height:1.4;color:var(--ink)}
</style>
</head>
<body>

<section class="spread outer">
  <div class="panel p1">
    <div class="head">
      <div class="brand"><span class="brand-mark"></span><span class="brand-name">Vostran, Pemmel &amp; Co.</span></div>
      <div class="tag">CERTIFIED PUBLIC ACCOUNTANTS</div>
    </div>
    <div class="copy">
      <p>Vostran, Pemmel &amp; Co. is a full service accounting firm serving clients across the region since 1975.</p>
      <p>Our team brings decades of hands-on experience and close personal attention to every engagement, large or small.</p>
      <p>We work with individuals and organizations in many fields, including:</p>
    </div>
    <ul class="bullets">
      <li>Medical practices</li>
      <li>Construction</li>
      <li>Retail and wholesale</li>
      <li>Non-profit organizations</li>
      <li>Real estate</li>
    </ul>
    <div class="photo" role="img" aria-label="Photo of stacked gold coins"></div>
  </div>

  <div class="panel p2">
    <div class="photo" role="img" aria-label="Photo of a person working through financial papers"></div>
    <div class="body">
      <div class="title">accounting</div>
      <div class="subtitle">services</div>
      <ul class="checks">
        <li><svg width="11" height="11" viewBox="0 0 11 11"><rect x=".5" y=".5" width="10" height="10" fill="none" stroke="#d9772b"/><path d="M2 5.5l2.5 2.5L9 2.5" fill="none" stroke="#3f2415" stroke-width="1.4"/></svg>Ledgerfox® Financial Software Support &amp; Consultations</li>
        <li><svg width="11" height="11" viewBox="0 0 11 11"><rect x=".5" y=".5" width="10" height="10" fill="none" stroke="#d9772b"/><path d="M2 5.5l2.5 2.5L9 2.5" fill="none" stroke="#3f2415" stroke-width="1.4"/></svg>Payroll Services</li>
        <li><svg width="11" height="11" viewBox="0 0 11 11"><rect x=".5" y=".5" width="10" height="10" fill="none" stroke="#d9772b"/><path d="M2 5.5l2.5 2.5L9 2.5" fill="none" stroke="#3f2415" stroke-width="1.4"/></svg>Accounting and Bookkeeping Services</li>
        <li><svg width="11" height="11" viewBox="0 0 11 11"><rect x=".5" y=".5" width="10" height="10" fill="none" stroke="#d9772b"/><path d="M2 5.5l2.5 2.5L9 2.5" fill="none" stroke="#3f2415" stroke-width="1.4"/></svg>Financial Statement Preparation</li>
        <li><svg width="11" height="11" viewBox="0 0 11 11"><rect x=".5" y=".5" width="10" height="10" fill="none" stroke="#d9772b"/><path d="M2 5.5l2.5 2.5L9 2.5" fill="none" stroke="#3f2415" stroke-width="1.4"/></svg>AP Management</li>
        <li><svg width="11" height="11" viewBox="0 0 11 11"><rect x=".5" y=".5" width="10" height="10" fill="none" stroke="#d9772b"/><path d="M2 5.5l2.5 2.5L9 2.5" fill="none" stroke="#3f2415" stroke-width="1.4"/></svg>AR Management</li>
      </ul>
    </div>
  </div>

  <div class="panel back">
    <div class="band"><p>Providing <span>Accounting, Financial, and Tax Services</span> Since 1975</p></div>
    <div class="addr">
      Vostran, Pemmel &amp; Co.<br>
      2184 Harlow Avenue, Suite 210<br>
      Brenmoor, OH 44091<br>
      Telephone: (555) 013-4821<br>
      info@vostranpemmel.com
    </div>
    <div class="photo map" role="img" aria-label="Street map showing the office location"></div>
    <div class="badge"></div>
    <div class="web">www.vostranpemmel.com</div>
  </div>

  <div class="panel front">
    <div class="brand"><span class="brand-mark"></span><span class="brand-name">Vostran, Pemmel &amp; Co.</span></div>
    <div class="claim">Certified Public Accountants and Business Advisors</div>
    <div class="photo" role="img" aria-label="Photo of a hand signing documents beside a calculator"></div>
    <div class="names">JAMES R. VOSTRAN, CPA<br>JOHN A. PEMMEL, CPA<br>TOBIN W. ARDEN, CPA</div>
    <div class="web">www.vostranpemmel.com</div>
  </div>
</section>

<section class="spread inner">
  <div class="panel p3">
    <div class="head">
      <div class="title">tax</div>
      <div class="subtitle">services</div>
    </div>
    <div class="photo" role="img" aria-label="Photo of a calculator on tax forms"></div>
    <ul class="bullets">
      <li>1040/Non-Profits</li>
      <li>1120/1120S/All Corp</li>
      <li>1065/LLC</li>
      <li>990/5500</li>
      <li>IRS Representation</li>
      <li>Tax Planning &amp; Strategies</li>
    </ul>
    <div class="client copy">
      <h3>Our Client</h3>
      <p>Individuals, corporations, partnerships, non-profit organizations, trusts, estates and small businesses rely on us for accurate and timely work.</p>
    </div>
  </div>

  <div class="panel p4">
    <div class="photo" role="img" aria-label="Photo of two business people shaking hands over papers"></div>
    <div class="strip"></div>
  </div>

  <div class="panel p5">
    <div class="head">
      <div class="title">turn-key accounting</div>
      <div class="subtitle">services</div>
    </div>
    <div class="rule"></div>
    <div class="copy">
      <p>Managing your books takes time away from running your business. Our turn-key service handles the daily details so you can focus on growth.</p>
      <p>We record transactions, reconcile accounts, manage payables and receivables, and deliver clear monthly reports you can act on.</p>
      <p>Our team sets up and supports your Ledgerfox files, trains your staff, and reviews your records to keep them clean and current.</p>
      <p>Whether you need full outsourced bookkeeping or periodic reviews, we shape the service around your needs and budget.</p>
      <p>Call us today to learn how a turn-key approach can save time and money.</p>
    </div>
  </div>

  <div class="panel p6">
    <div class="vertical">professional</div>
    <div class="title">staff</div>
    <div class="staff">
      <div class="member">
        <div class="portrait" role="img" aria-label="Portrait of James R. Vostran"></div>
        <div><h4>JAMES R. VOSTRAN, CPA</h4><p>Founded the firm in 1975 and leads tax planning and business advisory work for long-standing clients.</p></div>
      </div>
      <div class="member">
        <div class="portrait" role="img" aria-label="Portrait of John A. Pemmel"></div>
        <div><h4>JOHN A. PEMMEL, CPA</h4><p>Oversees audit and financial statement services with a focus on non-profit and corporate clients.</p></div>
      </div>
      <div class="member">
        <div class="portrait" role="img" aria-label="Portrait of Tobin W. Arden"></div>
        <div><h4>TOBIN W. ARDEN, CPA</h4><p>Manages bookkeeping, payroll and Ledgerfox support for small businesses and growing companies.</p></div>
      </div>
    </div>
  </div>
</section>

</body>
</html>
```